Bright Path Attorneys Billboard Design for Personal Injury Law Firm

Need a billboard design that we can use for different versions. 1400px X 400px jpeg or png
I have attached the logo and the attorney for the billboard. Attorney Marla Benning
Here is a link to our current website brightpathlegalgroup.example

HEADLINE: HIT BY A TRUCK?
SUBHEAD: NO FEE. BIG FIGHT.
877-GRANTLY

HEADLINE: ACCIDENT?
SUBHEAD: NO FEE, UNLESS WE WIN!
877-GRANTLY

HEADLINE: BIG TRUCK. BIG CASE.
SUBHEAD: YOU PAY $0 UPFRONT
877-GRANTLY

Target Market(s)

People in Car Accident

Industry/Entity Type

Personal Injury Attorneys

```html
<!DOCTYPE html>
<html lang="en">
<head>
<meta charset="utf-8">
<title>Bright Path Attorneys Billboards</title>
<link rel="stylesheet" href="https://fonts.googleapis.com/css2?family=Montserrat:wght@500;600;700;800&display=swap">
<style>
  :root {
    --page: #ffffff;
    --navy-deep: #0c1528;
    --navy-mid: #1a2b4d;
    --charcoal: #2a2b2e;
    --charcoal-light: #4a4c50;
    --ink: #ffffff;
    --green: #4fd84a;
  }
  * { margin: 0; padding: 0; box-sizing: border-box; }
  html, body {
    width: 1200px; height: 1200px; overflow: hidden;
    background: var(--page);
    font-family: "Montserrat", Arial, sans-serif;
    color: var(--ink);
  }
  .canvas { position: relative; width: 1200px; height: 1200px; }

  /* Each billboard keeps the 1400 x 400 proportion, shown at 75% scale */
  .billboard {
    position: absolute; left: 75px;
    width: 1050px; height: 300px;
    overflow: hidden;
  }
  .billboard > * { position: absolute; }

  .brand { display: flex; align-items: center; gap: 10px; }
  .brand-dot { width: 24px; height: 24px; border-radius: 50%; background: var(--green); flex: none; }
  .brand-name {
    font-size: 16px; font-weight: 600; color: var(--ink); line-height: 1.05;
    text-transform: uppercase; letter-spacing: 0.02em; white-space: nowrap;
  }

  .headline { font-weight: 800; line-height: 1; letter-spacing: -0.01em; white-space: nowrap; }
  .subhead { font-weight: 500; line-height: 1; letter-spacing: -0.01em; white-space: nowrap; }
  .phone { font-weight: 700; color: var(--green); line-height: 1; letter-spacing: -0.01em; white-space: nowrap; }

  /* Truck billboard */
  .board-truck {
    top: 75px;
    background: linear-gradient(160deg, var(--navy-mid) 0%, var(--navy-deep) 70%);
  }
  .board-truck .brand { left: 40px; top: 26px; }
  .board-truck .headline { left: 40px; top: 90px; font-size: 62px; }
  .board-truck .subhead { left: 40px; top: 170px; font-size: 30px; }
  .board-truck .phone { left: 40px; top: 216px; font-size: 64px; }

  /* Attorney billboard */
  .board-attorney {
    top: 450px;
    background: linear-gradient(100deg, var(--charcoal) 0%, var(--charcoal) 55%, var(--charcoal-light) 100%);
  }
  .attorney-portrait {
    left: 700px; top: 20px; width: 260px; height: 280px;
    border-radius: 130px 130px 0 0;
    background: linear-gradient(180deg, #8a6d55 0%, #1c2238 45%, #141a2c 100%);
  }
  .board-attorney .headline { left: 40px; top: 26px; font-size: 62px; }
  .board-attorney .brand { left: 200px; top: 98px; }
  .board-attorney .subhead { left: 40px; top: 152px; font-size: 26px; }
  .board-attorney .attorney-name { left: 40px; top: 206px; font-size: 14px; font-weight: 700; white-space: nowrap; }
  .board-attorney .phone { left: 40px; top: 230px; font-size: 56px; }

  /* Big case billboard */
  .board-case {
    top: 825px;
    background: #1e2022;
  }
  .truck-scene {
    left: 0; top: 0; width: 1050px; height: 300px;
    background:
      radial-gradient(ellipse 35% 60% at 60% 55%, #6a6d70 0%, rgba(60,62,65,0.6) 55%, transparent 100%),
      linear-gradient(180deg, #2a2c2f 0%, #3a3c3f 55%, #1c1d1f 100%);
  }
  .board-case .brand { left: 40px; top: 22px; }
  .board-case .headline { left: 40px; top: 70px; font-size: 56px; line-height: 1.02; }
  .board-case .subhead { left: 40px; top: 196px; font-size: 24px; }
  .board-case .phone { left: 40px; top: 234px; font-size: 50px; }
</style>
</head>
<body>
<main class="canvas">

  <section class="billboard board-truck">
    <div class="brand">
      <span class="brand-dot"></span>
      <span class="brand-name">Bright Path<br>Attorneys</span>
    </div>
    <h2 class="headline">HIT BY A TRUCK?</h2>
    <p class="subhead">NO FEE. BIG FIGHT.</p>
    <p class="phone">877-GRANTLY</p>
  </section>

  <section class="billboard board-attorney">
    <div class="attorney-portrait" role="img" aria-label="Portrait photo of attorney Marla Benning in a navy suit"></div>
    <h2 class="headline">ACCIDENT?</h2>
    <div class="brand">
      <span class="brand-dot"></span>
      <span class="brand-name">Bright Path<br>Attorneys</span>
    </div>
    <p class="subhead">NO FEE, UNLESS WE WIN!</p>
    <p class="attorney-name">ATTORNEY MARLA BENNING</p>
    <p class="phone">877-GRANTLY</p>
  </section>

  <section class="billboard board-case">
    <div class="truck-scene" role="img" aria-label="Photo of a white semi truck on a highway under a dark sky"></div>
    <div class="brand">
      <span class="brand-dot"></span>
      <span class="brand-name">Bright Path<br>Attorneys</span>
    </div>
    <h2 class="headline">BIG TRUCK.<br>BIG CASE.</h2>
    <p class="subhead">YOU PAY $0 UPFRONT</p>
    <p class="phone">877-GRANTLY</p>
  </section>

</main>
</body>
</html>
```